Client Referral Scheme

To design a brochure to advertise our client referral scheme.
Referees will be estate agents, architects, builders, tradesmen etc.
Front page: Tidewell Fittings Ltd with logo
Title: Client referral scheme
Quality German kitchens designed & installed
website address: www.tidewellfittings.example
white background, black, grey, yellow theme as per logo
Centre pages: How the scheme works (see attachment), pictures of kitchens from brenner kitchens
Back page: info about us from our website

" attachments below are my ideas, however I want them to be far classier as per the Pemberly interiors brochure

Industry/Entity Type

Builders

Requirements
Must have
• The refer mid document attached must be the middle page

```html
<!DOCTYPE html>
<html lang="en">
<head>
<meta charset="utf-8">
<title>Contractor Referral Scheme – Tidewell Fittings</title>
<link href="https://fonts.googleapis.com/css2?family=Comfortaa:wght@400;700&family=Great+Vibes&family=Nunito:wght@800&display=swap" rel="stylesheet">
<style>
:root{
  --yellow:#efcb1b;
  --yellow-soft:#f3d956;
  --cream:#f8eab3;
  --pale:#f9efc4;
  --brown:#7a5a1e;
  --brown-dark:#5e4312;
  --orange:#e8a23a;
  --orange-text:#e38f2c;
  --white:#fffdf3;
}
*{margin:0;padding:0;box-sizing:border-box}
html,body{width:1200px;height:874px;overflow:hidden;background:var(--white)}
body{font-family:'Comfortaa',sans-serif;color:var(--brown)}
.sheet{position:relative;width:1200px;height:874px;background:var(--yellow);overflow:hidden}
.abs{position:absolute}
.centre{text-align:center}

/* left panel */
.title-kicker{left:260px;top:70px;width:260px;font-size:20px;letter-spacing:12px;color:var(--white);font-weight:400}
.title-script{left:250px;top:88px;width:300px;font-family:'Great Vibes',cursive;font-size:96px;color:#f6e596;line-height:1}
.title-sub{left:400px;top:152px;font-size:38px;color:var(--white)}
.intro{left:173px;top:210px;width:400px;font-size:26px;line-height:33px;color:var(--brown)}
.network{left:76px;top:288px;width:370px;height:336px;border-radius:40px}
.badge{left:487px;top:272px;width:260px;height:260px}
.badge-kicker{left:487px;top:335px;width:260px;font-size:22px}
.badge-amount{left:487px;top:345px;width:260px;font-size:98px;color:var(--brown-dark);letter-spacing:-2px}
.award-tab{left:582px;top:464px;width:158px;height:48px;background:var(--orange);display:flex;align-items:center;justify-content:center;font-size:15px;color:var(--brown-dark)}
.award-hand{left:441px;top:465px;width:141px;height:95px;border-radius:30px}
.quote{left:520px;top:566px;width:210px;font-size:14px;line-height:17px}
.points{left:140px;top:660px;width:470px;list-style:none;font-size:19px;line-height:19px}
.points li{margin-bottom:4px}
.points li::before{content:"";display:inline-block;width:12px;height:12px;border-radius:50%;background:var(--orange);border:3px solid var(--pale);margin-right:6px;vertical-align:1px}
.points .highlight{color:var(--orange-text)}
.phone{left:140px;top:787px;width:470px;font-family:'Nunito',sans-serif;font-weight:800;font-size:20px;color:var(--brown-dark)}
.links{left:120px;top:812px;width:510px;font-size:15px;line-height:18px}
.divider{left:740px;top:6px;width:1px;height:860px;background:var(--brown)}
.dots{top:0;width:8px;height:874px;background:radial-gradient(circle,var(--pale) 2.5px,transparent 3px) 0 0/8px 9px repeat-y}

/* right panel */
.form-card{left:773px;top:0;width:392px;height:853px;background:var(--cream);border-radius:0 0 24px 24px}
.brand-ring{left:878px;top:29px;width:184px;height:184px;border-radius:50%;background:var(--pale);border:5px solid #fbf3d3}
.brand-name{left:878px;top:100px;width:184px;display:flex;align-items:center;justify-content:center;gap:6px;font-size:14px;font-weight:700;color:#8a8a8a}
.brand-name .mark{width:12px;height:12px;border-radius:50%;background:var(--yellow)}
.brand-tag{left:878px;top:122px;width:184px;font-size:7px;color:#a08e55}
.field-label{left:868px;width:200px;text-align:center}
.field-label span{background:var(--yellow);color:var(--white);font-size:14px;padding:1px 10px}
.rule{left:813px;width:311px;border-top:1.5px dotted var(--brown)}
.social{top:774px;width:36px;height:36px;border-radius:50%;background:var(--brown);border:2px solid var(--cream)}
.contacts{left:780px;top:819px;width:380px;font-size:9px;display:flex;justify-content:space-between;padding:0 8px}
</style>
</head>
<body>
<main class="sheet">
  <!-- left panel -->
  <div class="abs title-kicker centre">CONTRACTOR</div>
  <div class="abs title-script centre">Referral</div>
  <div class="abs title-sub">scheme</div>
  <h1 class="abs intro centre" style="font-weight:400">Claiming your referral reward couldn’t be simpler...</h1>

  <div class="abs network" role="img" aria-label="Illustration of contractors linked in a referral network, each earning a reward" style="background:radial-gradient(circle,#f5dd6a 0%,#f0cf2a 70%,var(--yellow) 100%)"></div>

  <svg class="abs badge" viewBox="0 0 260 260" aria-hidden="true">
    <circle cx="130" cy="130" r="128" fill="#f4dc67"/>
    <circle cx="130" cy="130" r="118" fill="#f6e28a"/>
    <circle cx="130" cy="130" r="108" fill="none" stroke="var(--orange)" stroke-width="2"/>
  </svg>
  <div class="abs badge-kicker centre">Claim upto</div>
  <div class="abs badge-amount centre">£250</div>
  <div class="abs award-tab">Referral Award</div>
  <div class="abs award-hand" role="img" aria-label="Illustration of a hand handing over banknotes" style="background:linear-gradient(120deg,#f0a83f,#fbe3b8)"></div>
  <p class="abs quote centre">“We’ll also donate £50 to Harbourlight Hospice with every referral received”.</p>

  <ul class="abs points centre">
    <li>Give someone you know the opportunity to benefit from an amazing ‘no hassle’ quality kitchen design and supply service.</li>
    <li class="highlight">Referral award upto £250</li>
    <li>Contribute and support a local charity</li>
  </ul>
  <p class="abs phone centre">Or Telephone: 804417</p>
  <p class="abs links centre">Instant form also online at: www.tidewellfittings.example/refer<br>more info: www.tidewellfittings.example</p>

  <div class="abs divider"></div>
  <div class="abs dots" style="left:750px"></div>
  <div class="abs dots" style="left:1176px"></div>

  <!-- right panel: referral form -->
  <section class="abs form-card"></section>
  <div class="abs brand-ring"></div>
  <div class="abs brand-name"><span class="mark"></span>Tidewell Fittings</div>
  <div class="abs brand-tag centre">quality kitchens, fitted well</div>

  <div class="abs field-label" style="top:243px"><span>Name</span></div>
  <div class="abs rule" style="top:288px"></div>
  <div class="abs field-label" style="top:290px"><span>Business Title</span></div>
  <div class="abs rule" style="top:344px"></div>
  <div class="abs field-label" style="top:346px"><span>Trade Type</span></div>
  <div class="abs rule" style="top:396px"></div>
  <div class="abs field-label" style="top:401px"><span>Name Of Referral</span></div>
  <div class="abs rule" style="top:449px"></div>
  <div class="abs field-label" style="top:452px"><span>Address Of Referral</span></div>
  <div class="abs rule" style="top:501px"></div>
  <div class="abs field-label" style="top:504px"><span>Phone Number</span></div>
  <div class="abs rule" style="top:553px"></div>
  <div class="abs field-label" style="top:557px"><span>Email Address</span></div>
  <div class="abs rule" style="top:607px"></div>
  <div class="abs field-label" style="top:609px"><span>Comments</span></div>
  <div class="abs rule" style="top:659px"></div>
  <div class="abs rule" style="top:689px"></div>
  <div class="abs rule" style="top:719px"></div>
  <div class="abs rule" style="top:748px"></div>

  <div class="abs social" style="left:918px"></div>
  <div class="abs social" style="left:951px"></div>
  <div class="abs social" style="left:984px"></div>
  <div class="abs contacts"><span>@tidewellfittings</span><span>info@tidewellfittings.example</span><span>@tidewellfit</span></div>
</main>
</body>
</html>
```